Business Card Design for Marketing Firm

Looking for business card design for higher end marketing firm. Clean but impressionable/trendy. We are a marketing firm that represents manufacturers in the foodservice equipment and supply industry. Our customers are end users such has hotels, restaurants, country clubs, convention centers and casinos as well as distributors of restaurants supplies and equipment, and manufacturers of foodservice equipment and supplies.
Target Market(s)
Hotels, Restaurants, Supply & Equipment Distributors, Foodservice Manufacturers
Industry/Entity Type
Foodservice/Hospitality
Contact Information for Business Card
Name, Title, Contact Number, Email, Website, Social Media, Address
Requirements
Must have
- Clean & Simple but Serious and Impressionable

```html
<!DOCTYPE html>
<html lang="en">
<head>
<meta charset="utf-8">
<title>Meridian Service Reps – Business Card</title>
<link rel="stylesheet" href="https://fonts.googleapis.com/css2?family=Open+Sans:wght@400;600;800&display=swap">
<style>
  :root {
    --stage: #3a3a3c;
    --navy: #2b2a78;
    --navy-deep: #1f1e66;
    --ink: #555559;
    --paper: #ffffff;
  }
  * { margin: 0; padding: 0; box-sizing: border-box; }
  html, body { width: 1200px; height: 689px; overflow: hidden; }
  body {
    background: var(--stage);
    font-family: "Open Sans", Arial, sans-serif;
    display: flex; align-items: center; justify-content: center; gap: 48px;
  }
  .card {
    width: 528px; height: 302px;
    box-shadow: 0 18px 40px rgba(0,0,0,.45);
    position: relative;
  }
  .card-back {
    background: var(--navy);
    display: flex; align-items: center; justify-content: center;
  }
  .back-wordmark {
    color: var(--navy-deep);
    font-weight: 600; font-size: 30px; letter-spacing: 2px;
  }
  .card-front { background: var(--paper); color: var(--ink); }
  .brand {
    position: absolute; left: 34px; top: 118px; width: 200px;
    color: var(--navy); font-weight: 600; font-size: 21px;
    line-height: 1.15; letter-spacing: 1px; text-transform: uppercase;
  }
  .brand-rule {
    position: absolute; left: 34px; top: 178px; width: 196px;
    height: 1.5px; background: var(--navy);
  }
  .divider {
    position: absolute; left: 258px; top: 44px; width: 1.5px; height: 178px;
    background: var(--navy);
  }
  .contact { position: absolute; left: 280px; top: 42px; }
  .person-name {
    color: var(--navy); font-weight: 800; font-size: 18px; letter-spacing: .5px;
    text-transform: uppercase;
  }
  .person-title { font-size: 13px; margin-bottom: 14px; }
  .address { font-size: 12.5px; line-height: 1.35; margin-bottom: 14px; }
  .line { display: flex; align-items: center; gap: 8px; font-size: 12.5px; line-height: 1.45; }
  .line svg { width: 11px; height: 11px; fill: var(--navy); flex: none; }
  .social {
    position: absolute; right: 26px; bottom: 26px;
    display: flex; align-items: center; gap: 8px; font-size: 13px;
  }
  .social-mark { width: 11px; height: 11px; background: var(--navy); border-radius: 2px; }
</style>
</head>
<body>
  <section class="card card-back">
    <span class="back-wordmark">MERIDIAN</span>
  </section>

  <section class="card card-front">
    <div class="brand">Meridian<br>Service Reps</div>
    <div class="brand-rule"></div>
    <div class="divider"></div>

    <div class="contact">
      <p class="person-name">Daniel Corwin</p>
      <p class="person-title">President</p>
      <p class="address">1840 Coastline Way<br>Bayview CA 90000</p>
      <p class="line">
        <svg viewBox="0 0 12 12"><path d="M3 1l2 2.5-1.2 1.2a7 7 0 0 0 3.5 3.5L8.5 7 11 9l-1.5 2C5 11 1 7 1 2.5z"/></svg>
        555-014-2278
      </p>
      <p class="line">
        <svg viewBox="0 0 12 12"><path d="M1 2.5h10v7H1z M1 2.5l5 4 5-4" stroke="#fff" stroke-width=".8"/></svg>
        info@meridianservicereps.com
      </p>
      <p class="line">
        <svg viewBox="0 0 12 12"><circle cx="6" cy="6" r="5"/><path d="M1 6h10M6 1c2 2.5 2 7.5 0 10M6 1c-2 2.5-2 7.5 0 10" stroke="#fff" stroke-width=".7" fill="none"/></svg>
        www.meridianservicereps.com
      </p>
    </div>

    <div class="social">
      <span class="social-mark"></span>
      @meridianservicereps
    </div>
  </section>
</body>
</html>
```